Painting Contractor Business Card Design

We are looking for a cool, bold, modern, polished, business card design. We are a high-end residential painting contractor. Please incorporate our logo and keep with our green/black color scheme. We are interested in seeing 2-sided and 1-sided options. Thank you very much!

Industry/Entity Type

Business

Contact Information for Business Card

Info for the card:
Owen Talsky
mobile 206-555-0193
email owen@kestrowfinish.net
web www.kestrowfinish.net

```html
<!DOCTYPE html>
<html lang="en">
<head>
<meta charset="utf-8">
<title>Kestrow Finish – Business Card</title>
<link href="https://fonts.googleapis.com/css2?family=Lato:wght@300;400;700;900&display=swap" rel="stylesheet">
<style>
  :root {
    --navy: #0b4f82;
    --blue: #1380c4;
    --teal: #2bb673;
    --lime: #c8d942;
    --sun: #f7b51c;
    --flame: #ef5a2a;
    --ink: #111111;
    --paper: #ffffff;
    --brand-green: #2aa84a;
    --backdrop: #e9e9e9;
  }
  * { box-sizing: border-box; margin: 0; padding: 0; }
  html, body {
    width: 1200px;
    height: 926px;
    overflow: hidden;
    background: var(--backdrop);
    font-family: "Lato", Arial, sans-serif;
  }
  .canvas {
    position: relative;
    width: 1200px;
    height: 926px;
  }
  .card {
    position: absolute;
    left: 250px;
    width: 700px;
    height: 400px;
    background: var(--paper);
    overflow: hidden;
    box-shadow: 0 6px 18px rgba(0,0,0,0.18);
  }
  .card--brand { top: 42px; }
  .card--contact { top: 484px; }

  /* Brand side */
  .colour-field {
    position: absolute;
    inset: 0;
    background: linear-gradient(100deg,
      var(--navy) 0%, var(--blue) 22%, var(--teal) 42%,
      var(--lime) 62%, var(--sun) 80%, var(--flame) 100%);
  }
  .dome {
    position: absolute;
    left: 100px;
    top: 170px;
    width: 500px;
    height: 500px;
    border-radius: 50%;
    background: var(--paper);
  }
  .brand-name {
    position: absolute;
    left: 0;
    right: 0;
    top: 268px;
    text-align: center;
    font-weight: 700;
    font-size: 36px;
    letter-spacing: 2px;
    color: var(--brand-green);
    white-space: nowrap;
  }
  .brand-name .brand-dot {
    display: inline-block;
    width: 26px;
    height: 26px;
    margin-right: 12px;
    background: var(--brand-green);
    vertical-align: -2px;
  }

  /* Contact side */
  .band {
    position: absolute;
    left: 0;
    right: 0;
    height: 24px;
    background: linear-gradient(90deg,
      var(--navy) 0%, var(--blue) 20%, var(--teal) 40%,
      var(--lime) 60%, var(--sun) 80%, var(--flame) 100%);
  }
  .band--top { top: 0; }
  .band--bottom { bottom: 0; }
  .mark-name {
    position: absolute;
    left: 70px;
    top: 118px;
    font-weight: 700;
    font-size: 30px;
    line-height: 1.1;
    letter-spacing: 1px;
    color: var(--brand-green);
  }
  .contact {
    position: absolute;
    left: 335px;
    top: 108px;
    color: var(--ink);
  }
  .contact__name {
    font-size: 36px;
    font-weight: 300;
    letter-spacing: 1px;
    margin-bottom: 8px;
  }
  .contact__name strong { font-weight: 900; }
  .contact__line {
    font-size: 22px;
    line-height: 1.35;
    font-weight: 400;
  }
  .contact__line--phone { font-size: 26px; }
  .contact__label { font-weight: 700; font-size: 18px; margin-right: 4px; }
</style>
</head>
<body>
<main class="canvas">
  <section class="card card--brand" aria-label="Card front">
    <div class="colour-field" role="img" aria-label="Multicolour painted stripe background in blue, green, yellow and orange"></div>
    <div class="dome"></div>
    <div class="brand-name"><span class="brand-dot"></span>KESTROW FINISH</div>
  </section>

  <section class="card card--contact" aria-label="Card back">
    <div class="band band--top" role="img" aria-label="Multicolour stripe border"></div>
    <div class="mark-name">KESTROW<br>FINISH</div>
    <div class="contact">
      <p class="contact__name">OWEN <strong>TALSKY</strong></p>
      <p class="contact__line contact__line--phone"><span class="contact__label">m.</span>206-555-0193</p>
      <p class="contact__line"><span class="contact__label">e.</span>owen@kestrowfinish.net</p>
      <p class="contact__line"><span class="contact__label">w.</span>www.kestrowfinish.net</p>
    </div>
    <div class="band band--bottom" role="img" aria-label="Multicolour stripe border"></div>
  </section>
</main>
</body>
</html>
```